Design our letter, business card, powerpoint and more

We have a logo and want a design for our business use. Letters (word template), business card (for printing) powerpoint presentation (template) and more.

```html
<!DOCTYPE html>
<html lang="en">
<head>
<meta charset="utf-8">
<title>Presentation Template Slides</title>
<link href="https://fonts.googleapis.com/css2?family=Maven+Pro:wght@400;500;600&display=swap" rel="stylesheet">
<style>
:root{
  --stage:#262626;
  --white:#ffffff;
  --tint:#edf4fe;
  --panel:#e6effc;
  --blue:#5aa8ec;
  --blue-soft:#8ec4f3;
  --ink:#2b2f36;
  --muted:#8a9099;
  --photo-a:#9aa3ad;
  --photo-b:#4a4f57;
}
*{margin:0;padding:0;box-sizing:border-box}
html,body{width:1200px;height:675px;overflow:hidden}
body{background:radial-gradient(ellipse at center,#3a3a3a 0%,var(--stage) 70%);font-family:'Maven Pro',sans-serif;color:var(--ink);position:relative}
.slide{position:absolute;width:361px;height:203px;border-radius:16px;overflow:hidden;background:var(--white)}
.slide--tint{background:var(--tint)}
.abs{position:absolute}
.heading{font-size:15px;font-weight:400;letter-spacing:.2px;line-height:1.2}
.dots{width:24px;height:8px}
.body{font-size:4.3px;line-height:1.65;color:var(--muted)}
.item-title{font-size:7.4px;font-weight:500;color:var(--ink)}
.photo{background:linear-gradient(160deg,var(--photo-a),var(--photo-b))}

/* profile */
.profile-photo{left:36px;top:36px;width:127px;height:131px;border-radius:2px;background:linear-gradient(170deg,#c7ccd1 0%,#7c848d 45%,#262b33 100%)}
.profile-name{left:192px;top:34px;font-size:15px;line-height:1.2}
.profile-role{left:192px;top:75px;font-size:4.5px;color:var(--ink);letter-spacing:.2px}
.quote{left:191px;top:107px;width:134px;height:60px;background:var(--panel);padding:11px 9px}
.quote-tail{left:176px;top:107px;width:16px;height:14px}

/* icon list */
.icon{width:9px;height:9px}

/* numbered cards */
.num-card{top:36px;width:92px;height:131px;background:var(--white);padding:10px 9px}
.num{font-size:14px;color:var(--blue)}
.num-sub{font-size:11px;margin-top:2px}
.num-body{margin-top:8px}
.btn{display:inline-block;margin-top:10px;background:var(--blue);color:var(--white);font-size:4px;padding:3px 5px;letter-spacing:.2px}

/* gallery */
.gal-card{top:36px;width:201px;height:131px;background:var(--white);padding:9px 12px}
.gal-card--faded{opacity:.35}
.gal-num{font-size:14px;color:var(--blue)}
.gal-sub{font-size:11px;margin-top:2px}
.gal-body{margin-top:6px}
.thumbs{position:absolute;left:12px;top:94px;display:flex;gap:8px}
.thumb{position:relative;width:39px;height:26px}
.badge{position:absolute;left:-3px;top:-4px;width:8px;height:8px;border-radius:50%;background:var(--blue);color:var(--white);font-size:4px;display:flex;align-items:center;justify-content:center}

/* title slide */
.hero-photo{left:0;top:0;width:161px;height:203px;background:linear-gradient(150deg,#d9d2c6 0%,#9c7a55 45%,#3c3129 100%)}
.arrow-btn{left:143px;top:83px;width:36px;height:36px;border-radius:50%;background:var(--blue);display:flex;align-items:center;justify-content:center}

/* numbered list */
.bullet{width:8px;height:8px;border-radius:50%;background:var(--blue);color:var(--white);font-size:4.5px;display:flex;align-items:center;justify-content:center}
</style>
</head>
<body>

<svg width="0" height="0" style="position:absolute">
  <defs>
    <symbol id="dots" viewBox="0 0 24 8">
      <circle cx="2.5" cy="4" r="2" fill="#5aa8ec"/>
      <circle cx="10" cy="4" r="3.8" fill="#5aa8ec"/>
      <line x1="10" y1="4" x2="20" y2="4" stroke="#5aa8ec" stroke-width="1.2"/>
      <circle cx="20.5" cy="4" r="2" fill="#5aa8ec"/>
    </symbol>
  </defs>
</svg>

<!-- Slide 1: profile -->
<section class="slide" style="left:36px;top:103px">
  <div class="abs profile-photo" role="img" aria-label="Portrait photo of a team member in a dark blazer"></div>
  <div class="abs profile-name">Daniel<br>Whitford</div>
  <div class="abs profile-role">DIRECTOR</div>
  <svg class="abs dots" style="left:192px;top:91px"><use href="#dots"/></svg>
  <svg class="abs quote-tail" viewBox="0 0 16 14"><polygon points="0,0 16,0 16,14" fill="#e6effc"/></svg>
  <div class="abs quote body">Ut enim ad minim veniam, quis nostrud exercitation ullamco laboris nisi ut aliquip ex ea commo conset. Duis aute irure dolor in reprehenderit in lorem ipsum dolor sit amet, consectetur sed adipiscing elit, sed do eiusmod tempor incididunt ut labore et dolore</div>
</section>

<!-- Slide 2: icon list -->
<section class="slide" style="left:420px;top:103px">
  <div class="abs heading" style="left:36px;top:30px">Icon list slides</div>
  <svg class="abs dots" style="left:36px;top:62px"><use href="#dots"/></svg>

  <svg class="abs icon" style="left:36px;top:83px" viewBox="0 0 10 10" fill="none" stroke="#5aa8ec" stroke-width="1"><circle cx="2.5" cy="2.5" r="1.6"/><circle cx="2.5" cy="7.5" r="1.6"/><line x1="3.8" y1="3.6" x2="9.5" y2="8.5"/><line x1="3.8" y1="6.4" x2="9.5" y2="1.5"/></svg>
  <div class="abs" style="left:51px;top:83px;width:125px">
    <div class="item-title">Subtitle text about project</div>
    <div class="body" style="margin-top:2px">Lorem ipsum dolor sit amet, consectetur adipiscing elit, sed do eiusmod tempor incididunt ut labore et dolore magna aliqua. Ut enim ad minim veniam, quis nostrud</div>
  </div>

  <svg class="abs icon" style="left:187px;top:83px" viewBox="0 0 10 10" fill="none" stroke="#5aa8ec" stroke-width="1"><rect x="1.5" y="1.5" width="7" height="8"/><rect x="3.5" y=".5" width="3" height="2" fill="#5aa8ec"/></svg>
  <div class="abs" style="left:202px;top:83px;width:125px">
    <div class="item-title">Subtitle text about project</div>
    <div class="body" style="margin-top:2px">Lorem ipsum dolor sit amet, consectetur adipiscing elit, sed do eiusmod tempor incididunt ut labore et dolore magna aliqua. Ut enim ad minim veniam, quis nostrud</div>
  </div>

  <svg class="abs icon" style="left:36px;top:132px" viewBox="0 0 10 10" fill="#5aa8ec"><polygon points="1,9 1.5,6.8 7.5,0.8 9.2,2.5 3.2,8.5"/></svg>
  <div class="abs" style="left:51px;top:132px;width:125px">
    <div class="item-title">Subtitle text about project</div>
    <div class="body" style="margin-top:2px">Lorem ipsum dolor sit amet, consectetur adipiscing elit, sed do eiusmod tempor incididunt ut labore et dolore magna aliqua. Ut enim ad minim veniam, quis nostrud</div>
  </div>

  <svg class="abs icon" style="left:187px;top:131px" viewBox="0 0 10 10" fill="none" stroke="#5aa8ec" stroke-width="1"><rect x="3" y="2.5" width="6" height="7"/><polyline points="1,7.5 1,.5 6.5,.5"/></svg>
  <div class="abs" style="left:202px;top:132px;width:125px">
    <div class="item-title">Subtitle text about project</div>
    <div class="body" style="margin-top:2px">Lorem ipsum dolor sit amet, consectetur adipiscing elit, sed do eiusmod tempor incididunt ut labore et dolore magna aliqua. Ut enim ad minim veniam, quis nostrud</div>
  </div>
</section>

<!-- Slide 3: numbered cards -->
<section class="slide slide--tint" style="left:804px;top:103px">
  <div class="abs num-card" style="left:36px">
    <div class="num">01</div>
    <div class="num-sub">Subtitle text</div>
    <div class="body num-body">Lorem ipsum sed dolor sit sed amet, consectetur adipiscing elit, sed do eiusmod tempor incididunt ut labore et dolore minim veniam, laboris quis nostrud exercitation ullamco</div>
    <span class="btn">MORE INFORMATION</span>
  </div>
  <div class="abs num-card" style="left:134px">
    <div class="num">02</div>
    <div class="num-sub">Subtitle text</div>
    <div class="body num-body">Lorem ipsum sed dolor sit sed amet, consectetur adipiscing elit, sed do eiusmod tempor incididunt ut labore et dolore minim veniam, laboris quis nostrud exercitation ullamco</div>
    <span class="btn">MORE INFORMATION</span>
  </div>
  <div class="abs num-card" style="left:232px">
    <div class="num">03</div>
    <div class="num-sub">Subtitle text</div>
    <div class="body num-body">Lorem ipsum sed dolor sit sed amet, consectetur adipiscing elit, sed do eiusmod tempor incididunt ut labore et dolore minim veniam, laboris quis nostrud exercitation ullamco</div>
    <span class="btn">MORE INFORMATION</span>
  </div>
</section>

<!-- Slide 4: gallery carousel -->
<section class="slide slide--tint" style="left:36px;top:349px">
  <div class="abs gal-card gal-card--faded" style="left:-127px">
    <div class="gal-num">01</div>
    <div class="gal-sub">Subtitle text about project</div>
    <div class="body gal-body">Lorem ipsum sed dolor sit amet, consectetur adipiscing elit, sed quis do eiusmod tempor incididunt minim veniam, laboris quis nostrud exercitation ut labore et dolore magna aliqua. Ut enim ullamco</div>
    <div class="thumbs">
      <div class="thumb photo" role="img" aria-label="Team meeting photo"><span class="badge">1</span></div>
      <div class="thumb photo" role="img" aria-label="Event hall photo"><span class="badge">2</span></div>
      <div class="thumb photo" role="img" aria-label="Office photo"><span class="badge">3</span></div>
      <div class="thumb photo" role="img" aria-label="Mountain lake photo" style="background:linear-gradient(180deg,#c9d6de,#5e7a6a)"><span class="badge">4</span></div>
    </div>
  </div>

  <div class="abs gal-card" style="left:80px">
    <div class="gal-num">02</div>
    <div class="gal-sub">Subtitle text about project</div>
    <div class="body gal-body">Lorem ipsum sed dolor sit sed amet, consectetur adipiscing elit, sed quis do eiusmod tempor incididunt ut labore et dolore minim veniam, laboris quis nostrud exercitation ullamco d tempor incididunt ut labore et dolore magna aliqua. Ut enim ad minim veniam, laboris quis nostrud exercitation ullamco</div>
    <div class="thumbs">
      <div class="thumb" role="img" aria-label="Team meeting photo" style="background:linear-gradient(160deg,#b9b2a6,#3b3832)"><span class="badge">1</span></div>
      <div class="thumb" role="img" aria-label="Event hall with stage lights photo" style="background:linear-gradient(180deg,#1c2433,#b8562c)"><span class="badge">2</span></div>
      <div class="thumb" role="img" aria-label="Colleagues at a table photo" style="background:linear-gradient(160deg,#cfc7b9,#5a4634)"><span class="badge">3</span></div>
      <div class="thumb" role="img" aria-label="Mountain lake landscape photo" style="background:linear-gradient(180deg,#b9cbd6,#3f5a45)"><span class="badge">4</span></div>
    </div>
  </div>

  <div class="abs gal-card gal-card--faded" style="left:288px">
    <div class="gal-num">03</div>
    <div class="gal-sub">Subtitle text about project</div>
    <div class="body gal-body">Lorem ipsum sed dolor sit amet, consectetur eiusmod tempor incididunt exercitation ullamco d tempor ad minim veniam, laboris quis</div>
    <div class="thumbs">
      <div class="thumb photo" role="img" aria-label="Team meeting photo"><span class="badge">1</span></div>
      <div class="thumb photo" role="img" aria-label="Event hall photo"><span class="badge">2</span></div>
    </div>
  </div>
</section>

<!-- Slide 5: title slide -->
<section class="slide slide--tint" style="left:420px;top:349px">
  <div class="abs hero-photo" role="img" aria-label="Photo of smiling colleagues working together at a table with a laptop"></div>
  <div class="abs arrow-btn">
    <svg width="13" height="13" viewBox="0 0 12 12" fill="none" stroke="#fff" stroke-width="1.3" stroke-linecap="round" stroke-linejoin="round"><line x1="1.5" y1="6" x2="10.5" y2="6"/><polyline points="6.5,2 10.5,6 6.5,10"/></svg>
  </div>
  <div class="abs heading" style="left:200px;top:62px">Title text slide</div>
  <div class="abs body" style="left:201px;top:86px;width:122px">Ut enim ad minim veniam, quis nostrud exercitation ullamco laboris nisi ut aliquip ex ea commo consequat. Duis aute irure dolor in reprehenderit in Lorem ipsum dolor sit amet, consectetur sed adipiscing elit, sed do eiusmod tempor incididunt ut labore et dolore magna aliqua. Voluptate velit esse cillum dolore eu fugiat nulla pariatur. Excepteur sint occaecat cupidatat non proiden</div>
</section>

<!-- Slide 6: numbered list -->
<section class="slide" style="left:804px;top:349px">
  <div class="abs heading" style="left:36px;top:32px">Numbered list</div>
  <svg class="abs dots" style="left:36px;top:62px"><use href="#dots"/></svg>

  <div class="abs bullet" style="left:36px;top:84px">1</div>
  <div class="abs" style="left:50px;top:84px;width:125px">
    <div class="item-title">Subtitle text about project</div>
    <div class="body" style="margin-top:2px">Lorem ipsum dolor sit amet, consectetur adipiscing elit, sed do eiusmod tempor incididunt ut labore et dolore magna aliqua. Ut enim ad minim veniam, quis nostrud</div>
  </div>

  <div class="abs bullet" style="left:187px;top:84px">3</div>
  <div class="abs" style="left:201px;top:84px;width:125px">
    <div class="item-title">Subtitle text about project</div>
    <div class="body" style="margin-top:2px">Lorem ipsum dolor sit amet, consectetur adipiscing elit, sed do eiusmod tempor incididunt ut labore et dolore magna aliqua. Ut enim ad minim veniam, quis nostrud</div>
  </div>

  <div class="abs bullet" style="left:36px;top:133px">2</div>
  <div class="abs" style="left:50px;top:133px;width:125px">
    <div class="item-title">Subtitle text about project</div>
    <div class="body" style="margin-top:2px">Lorem ipsum dolor sit amet, consectetur adipiscing elit, sed do eiusmod tempor incididunt ut labore et dolore magna aliqua. Ut enim ad minim veniam, quis nostrud</div>
  </div>

  <div class="abs bullet" style="left:187px;top:133px">4</div>
  <div class="abs" style="left:201px;top:133px;width:125px">
    <div class="item-title">Subtitle text about project</div>
    <div class="body" style="margin-top:2px">Lorem ipsum dolor sit amet, consectetur adipiscing elit, sed do eiusmod tempor incididunt ut labore et dolore magna aliqua. Ut enim ad minim veniam, quis nostrud</div>
  </div>
</section>

</body>
</html>
```